Quarrel Ridge Advisory Business Card

Quarrel Ridge Advisory is a company that provides consulting services to the Mining Industry.

Whilst Quarrel Ridge Advisory is an Australian based company its client base is the global mining industry.

The essence of Quarrel Ridge Advisory is its a can do organisation that can make a difference to its clients by providing quality assistance and form lasting relationships.
Updates

Target Market(s)

The global Mining Industry.

Industry/Entity Type

Mining

Font styles to use
Serif

Colors

Designer to choose colors to be used in the design.

Requirements
Nice to have
• My thinking is the card would look good in black given the logo.

I would like to see written on the back side of the card " Providing Metallurgical, Management and Corporate Services to the Mining Industry"

```html
<!DOCTYPE html>
<html lang="en">
<head>
<meta charset="utf-8">
<title>Quarrel Ridge Advisory — Business Card</title>
<link rel="stylesheet" href="https://fonts.googleapis.com/css2?family=Questrial&display=swap">
<style>
  :root {
    --backdrop: #e6e6e6;
    --card-white: #ffffff;
    --accent-orange: #f39a2b;
    --slate: #4f5053;
    --slate-light: #606164;
    --slate-dark: #3c3d3f;
    --text-light: #f2f2f2;
  }
  * { margin: 0; padding: 0; box-sizing: border-box; }
  html, body {
    width: 1200px; height: 720px; overflow: hidden;
    background: var(--backdrop);
    font-family: "Questrial", "Century Gothic", sans-serif;
  }
  .canvas { position: relative; width: 1200px; height: 720px; }

  .card {
    position: absolute; top: 241px;
    width: 420px; height: 240px;
    overflow: hidden;
  }
  .card--front { left: 147px; background: var(--card-white); }
  .card--back {
    left: 633px;
    background: linear-gradient(160deg, var(--slate-light) 0%, var(--slate) 45%, var(--slate-dark) 100%);
  }

  /* Front */
  .brand-name {
    position: absolute; left: 0; right: 0; top: 68px;
    text-align: center;
    color: var(--accent-orange);
    font-size: 34px; line-height: 38px;
    letter-spacing: 1px;
    text-transform: uppercase;
  }
  .contact-icons {
    position: absolute; left: 0; right: 0; top: 187px;
    height: 14px;
  }
  .contact-icons svg { position: absolute; top: 0; }
  .icon-mail { left: 71px; }
  .icon-phone { left: 206px; }
  .icon-web { left: 330px; }

  .contact-band {
    position: absolute; left: 0; right: 0; bottom: 0; height: 39px;
    background: var(--slate);
    border-top: 2px solid var(--accent-orange);
    display: flex; align-items: center; justify-content: space-between;
    padding: 0 14px 4px 14px;
    color: var(--text-light);
    font-size: 12px; letter-spacing: 0.3px;
  }

  /* Back */
  .back-name {
    position: absolute; left: 0; right: 0; top: 70px;
    text-align: center;
    color: var(--text-light);
    font-size: 18px; letter-spacing: 3px;
    text-transform: uppercase;
  }
  .tagline {
    position: absolute; left: 0; right: 0; top: 114px;
    text-align: center;
    color: var(--text-light);
    font-size: 12px; line-height: 19px;
    letter-spacing: 0.2px;
  }
</style>
</head>
<body>
<main class="canvas">

  <section class="card card--front" aria-label="Business card front">
    <h1 class="brand-name">Quarrel Ridge<br>Advisory</h1>

    <div class="contact-icons" aria-hidden="true">
      <svg class="icon-mail" width="14" height="11" viewBox="0 0 14 11">
        <rect x="0.75" y="0.75" width="12.5" height="9.5" fill="none" stroke="#f39a2b" stroke-width="1.2"/>
        <path d="M0.75 0.75 L7 6 L13.25 0.75 M0.75 10.25 L5.2 4.6 M13.25 10.25 L8.8 4.6" fill="none" stroke="#f39a2b" stroke-width="1.1"/>
      </svg>
      <svg class="icon-phone" width="8" height="13" viewBox="0 0 8 13">
        <rect x="0.7" y="2" width="6.6" height="10.3" rx="1" fill="none" stroke="#f39a2b" stroke-width="1.2"/>
        <line x1="2" y1="0" x2="2" y2="2" stroke="#f39a2b" stroke-width="1.2"/>
        <rect x="2" y="3.6" width="4" height="3" fill="#f39a2b"/>
      </svg>
      <svg class="icon-web" width="12" height="12" viewBox="0 0 12 12">
        <circle cx="6" cy="6" r="5.3" fill="none" stroke="#f39a2b" stroke-width="1.1"/>
        <ellipse cx="6" cy="6" rx="2.4" ry="5.3" fill="none" stroke="#f39a2b" stroke-width="1"/>
        <line x1="0.7" y1="6" x2="11.3" y2="6" stroke="#f39a2b" stroke-width="1"/>
      </svg>
    </div>

    <footer class="contact-band">
      <span class="contact-email">hello@quarrelridge.com</span>
      <span class="contact-phone">555-014-2730</span>
      <span class="contact-web">www.quarrelridge.com</span>
    </footer>
  </section>

  <section class="card card--back" aria-label="Business card back">
    <p class="back-name">Quarrel Ridge Advisory</p>
    <p class="tagline">Providing Metallurgical, Management and Corporate<br>Services to the Mining Industry</p>
  </section>

</main>
</body>
</html>
```